依頼詳細
■商品のアピールポイント・特徴
薬剤師が開発
ヨモギなど生薬が主成分
添加物不使用
発泡剤・界面活性剤・防腐剤・安定剤不使用
飲み込んでも安全
緑色のジェル
ミントの香り
価格 2000円前後予定

■商品のネーミング
Tovelique (※読み方:トヴェリーク)

○ネーミング由来
pharmacist(薬剤師さん)+natural(自然派)+mint(ミントの香り)
女性らしいやさしい響きです。

■開発元会社紹介
110年続く漢方薬舗

■ターゲット(ペルソナ)
30〜50代女性

■パッケージデザイン
デザイン案の目安として、社内女性陣に多数決をおこなったところ、添付PDFのモノトーン系の①⑨⑤が好評でした。
また、商品写真を見ていただくと分かりますが、中身が緑色をしています。(わさびに似ていますが…)
また、商品名にもミントと付いていますので、デザインのベースはモノトーンでワンポイント的に緑があるのもいいかなと考えていますが、まだその辺りは未定です。
モノトーンのみのデザインでもデザインによっては良いかもしれません。

※商品名は必ずデザインに掲載お願い致します。英語表記限定→【Tovelique】

■パッケージのポイント
ターゲットが女性で、ポーチの中で持ち歩き、外で友人の前で取り出したとしても恥ずかしくないデザイン。パッケージ自体は小さいので、化粧品のようなデザインでもアリかな。と考えています。

■お客様に与えたい印象
パッケージがおしゃれ。商品自体がおしゃれで気軽にポーチに持ち運べる。
薬剤師が開発した自然派の塗り薬だから安心して使える。

■ 重視する点/検討基準
何故そのデザインになったのか。その理由・ストーリー
記載項目
データでは、肩下サイズ60mmと記載されておりますが、
実際には88mmとなります。
肩下サイズは88mmにて作成下さいますようお願い申し上げます。
Φ19×88mm
添付資料の方御覧ください。
希望イメージ
シンプル 複雑
単色 カラフル
暗い 明るい
日常 高級
遊び心 厳粛
未来的 伝統的
女性的 男性的
希望する色
緑系、グレー系
納品ファイル
• 高解像度JPG (.jpg)
• イラストレーター形式 (.ai)
• フォトショップ形式 (.psd)
補足説明
パッケージ裏面には製品概要・成分表・弊社情報・連絡先等が入りますので、枠の作成をお願い致します。
依頼、デザインご提案の際に不備・疑問点などございましたら、お気軽にご連絡頂ければ幸いです。ご回答させていただきます。
すみません、提案数の関係で、提案の締め切りを少し延長させていただきます。

コンセプトとデザインが非常にマッチしており選ばせて頂きました!

今回、沢山のご提案を頂きありがとうございました!
お陰様で良い商品になりそうです。
今後共よろしくお願い申し上げますm(_ _)m

```html
<!DOCTYPE html>
<html lang="en">
<head>
<meta charset="utf-8">
<title>Clean Smile Every Day – Tovelique</title>
<link href="https://fonts.googleapis.com/css2?family=Tinos:wght@400;700&family=Roboto:wght@400&display=swap" rel="stylesheet">
<style>
  :root {
    --backdrop: #f4f5f5;
    --tube: #eef3f4;
    --tube-edge: #dfe6e8;
    --seal: #f7f9f9;
    --cap: #f8f9f9;
    --ink: #1d1d1d;
    --ink-soft: #3a3a3a;
    --ornament: #d9dfe0;
    --leaf-light: #8cc48a;
    --leaf-dark: #3f8a4a;
  }
  * { margin: 0; padding: 0; box-sizing: border-box; }
  html, body {
    width: 800px;
    height: 1200px;
    overflow: hidden;
    background: var(--backdrop);
  }
  .canvas {
    position: relative;
    width: 800px;
    height: 1200px;
  }
  .tube-shape {
    position: absolute;
    left: 0;
    top: 0;
  }
  .label {
    position: absolute;
    left: 165px;
    width: 470px;
    top: 0;
    height: 1200px;
    text-align: center;
    color: var(--ink);
  }
  .headline {
    position: absolute;
    top: 205px;
    width: 100%;
    font-family: "Tinos", serif;
    font-weight: 400;
    font-size: 70px;
    line-height: 80px;
    letter-spacing: 2px;
  }
  .product-name {
    position: absolute;
    top: 548px;
    width: 100%;
    font-family: "Tinos", serif;
    font-size: 40px;
    font-weight: 700;
    color: var(--ink-soft);
  }
  .ornament {
    position: absolute;
    top: 630px;
    left: 200px;
    width: 70px;
    height: 20px;
    border-radius: 10px;
    background: var(--ornament);
  }
  .claim {
    position: absolute;
    top: 700px;
    width: 100%;
    font-family: "Tinos", serif;
    font-size: 28px;
    line-height: 36px;
    color: var(--ink-soft);
  }
  .mint-leaf {
    position: absolute;
    top: 832px;
    left: 195px;
    width: 80px;
    height: 80px;
    border-radius: 60% 10% 60% 10%;
    background: linear-gradient(135deg, var(--leaf-light), var(--leaf-dark));
  }
  .notes {
    position: absolute;
    top: 938px;
    width: 100%;
    font-family: "Roboto", sans-serif;
    font-size: 19px;
    line-height: 36px;
    color: var(--ink-soft);
  }
</style>
</head>
<body>
<main class="canvas">
  <svg class="tube-shape" width="800" height="1200" viewBox="0 0 800 1200" aria-hidden="true">
    <rect class="tube-seal" x="158" y="12" width="484" height="120" rx="6" fill="var(--seal)" stroke="var(--tube-edge)" stroke-width="2"/>
    <path class="tube-body" d="M162 130 H638 L612 1050 H188 Z" fill="var(--tube)" stroke="var(--tube-edge)" stroke-width="2"/>
    <rect class="tube-cap" x="196" y="1048" width="408" height="128" rx="16" fill="var(--cap)" stroke="var(--tube-edge)" stroke-width="2"/>
  </svg>

  <section class="label">
    <h1 class="headline">CLEAN<br>SMILE<br>EVERY<br>DAY</h1>
    <p class="product-name">Tovelique</p>
    <div class="ornament" role="img" aria-label="Small decorative flourish"></div>
    <p class="claim">Tooth paste<br>developed<br>by a pharmacist</p>
    <div class="mint-leaf" role="img" aria-label="Illustration of a fresh mint leaf"></div>
    <p class="notes">Mint-Flavored<br>Additive not used</p>
  </section>
</main>
</body>
</html>
```